Biz Card for Harrowfield Property Partners - HWPP

Harrowfield Property Partners is a commercial real estate acquisitions firm. We buy commercial property and need to raise capital from investors for each deal we buy. The vibe needs to be: give us your money, we will multiply it.
Our website: www.hrwpp-example.com
Competitors are: https://velmarholdings-example.com/, https://tribanquepartners-example.com/, http://www.ostrellecapital-example.com/
Target Market(s)
High Net Worth Individuals, Bankers, Insurance Companies, Commercial Real Estate Brokers.
Industry/Entity Type
Investment Banking
Contact Information for Business Card
Name, Title, Addess, Cell#, Office#, email, website
Requirements
Must have
- use one of our logos. See website for look and feel: www.hrwpp-example.com
Nice to have
- see website: www.hrwpp-example.com

```html
<!DOCTYPE html>
<html lang="en">
<head>
<meta charset="utf-8">
<title>Harrowfield Property Partners – Business Card</title>
<link href="https://fonts.googleapis.com/css2?family=Work+Sans:wght@400;500;600&display=swap" rel="stylesheet">
<style>
  :root {
    --backdrop: #0e0e0e;
    --card: #232323;
    --card-edge: #2b2b2b;
    --silver: #bdbdbd;
    --silver-soft: #a6a6a6;
    --divider: #8a8a8a;
  }
  * { margin: 0; padding: 0; box-sizing: border-box; }
  html, body {
    width: 1200px; height: 900px; overflow: hidden;
    background: var(--backdrop);
    font-family: "Work Sans", sans-serif;
  }
  .stage {
    width: 1200px; height: 900px;
    display: flex; flex-direction: column; align-items: center; justify-content: center;
    gap: 40px;
  }
  .card {
    width: 700px; height: 400px;
    background: linear-gradient(135deg, var(--card) 0%, var(--card-edge) 100%);
    box-shadow: 0 18px 40px rgba(0,0,0,.6);
    position: relative;
  }
  .card--front {
    display: flex; flex-direction: column; align-items: center; justify-content: center;
    gap: 26px;
  }
  .brand-mark {
    border-radius: 50%;
    background: var(--silver);
  }
  .card--front .brand-mark { width: 100px; height: 100px; }
  .brand-name {
    color: var(--silver);
    font-weight: 500;
    text-transform: uppercase;
  }
  .card--front .brand-name { font-size: 26px; letter-spacing: 6px; }

  .card--back {
    display: flex; align-items: center;
    padding: 0 50px 0 60px;
  }
  .back-brand {
    display: flex; align-items: center; gap: 18px;
    width: 340px;
  }
  .card--back .brand-mark { width: 72px; height: 72px; flex: none; }
  .card--back .brand-name { font-size: 17px; letter-spacing: 4px; line-height: 1.5; width: 240px; }
  .divider {
    width: 1.5px; height: 220px; background: var(--divider);
    margin: 0 34px 0 10px;
  }
  .contact { color: var(--silver); }
  .contact__name { font-size: 20px; font-weight: 600; letter-spacing: 1px; text-transform: uppercase; }
  .contact__title { font-size: 17px; color: var(--silver-soft); margin-top: 4px; }
  .contact__address { font-size: 17px; line-height: 1.3; margin-top: 16px; }
  .contact__lines { list-style: none; margin-top: 12px; font-size: 17px; line-height: 1.45; }
  .contact__lines li { display: flex; align-items: center; gap: 8px; }
  .contact__lines svg { width: 13px; height: 13px; flex: none; stroke: var(--silver); fill: none; stroke-width: 1.6; }
</style>
</head>
<body>
<main class="stage">
  <section class="card card--front" aria-label="Card front">
    <div class="brand-mark" aria-hidden="true"></div>
    <p class="brand-name">Harrowfield Property Partners</p>
  </section>

  <section class="card card--back" aria-label="Card back">
    <div class="back-brand">
      <div class="brand-mark" aria-hidden="true"></div>
      <p class="brand-name">Harrowfield Property Partners</p>
    </div>
    <div class="divider" aria-hidden="true"></div>
    <div class="contact">
      <p class="contact__name">Daniel Ostrow</p>
      <p class="contact__title">Founder</p>
      <p class="contact__address">418 Marlowe Ave,<br>Suite 900 Pinecrest<br>Bay, FL 33190</p>
      <ul class="contact__lines">
        <li>
          <svg viewBox="0 0 16 16" aria-hidden="true"><path d="M4 1.5l2.2 3-1.4 1.6a9 9 0 0 0 5.1 5.1l1.6-1.4 3 2.2-1.2 2.2C8 14 2 8 1.8 2.7z"/></svg>
          (555) 014-2297
        </li>
        <li>
          <svg viewBox="0 0 16 16" aria-hidden="true"><rect x="1.5" y="3.5" width="13" height="9"/><path d="M1.5 3.5l6.5 5 6.5-5"/></svg>
          info@hrwpp-example.com
        </li>
        <li>
          <svg viewBox="0 0 16 16" aria-hidden="true"><circle cx="8" cy="8" r="6.5"/><ellipse cx="8" cy="8" rx="2.8" ry="6.5"/><path d="M1.5 8h13"/></svg>
          www.hrwpp-example.com
        </li>
      </ul>
    </div>
  </section>
</main>
</body>
</html>
```